Glenmorrow ice cream tub packaging

We need new tub designs for our dairy free ice cream. It is made with avocado and coconut which we would like communicated within the design. We launched last year and have had positive feedback regarding our current packaging but also that it could be a cleaner design with a more sophisticated font as it will be sold in more high end expensive stores. I have attached our current packaging for info (there are 3 flavours - Original Avocado, Raspberry and Basil, Raw Cacao) We would like to keep the avocado print that is currently included on the packaging as we have had a lot of very positive feedback about that. Maybe not as much though as it makes it quite busy and we prefer a clean design.
I've also attached our new logo.
We would like it to mention we are gluten, soya, dairy, egg and nut free. And that it is a 'coconut and avocado ice cream' rather than an 'alternative'.
The nutritional label needs to be in a UK table format (I've attached a blank copy for information). We don't currently have the values for the table as it has been sent off for testing as we have a new recipe. But if you could leave that blank we will fill it in when we have the results.
I've attached the template for the sizes as we have two sizes - 500ml and 100ml. The designs will be the same but just smaller/bigger. It has to be font size 11 for legal purpose.
It has to have the weight (100ml and 500ml) followed by the official e-mark.
The ingredients are the same but take out Locust Bean Gum and replace Vanilla extract with Lime Juice.
The business address is the same but should read 'Glenmorrow LTD'. All other info on the packaging (barcode, text etc) is to remain the same.
I've have also attached 3 pictures of other tub designs that we like for inspiration - our favourite is 'zelt' as we can have half the print half the colour if the flavour (raspberry/pink, cacao/brown, original/green)
Updates
Target Market(s)
High end health food stores
Look and feel

```html
<!DOCTYPE html>
<html lang="en">
<head>
<meta charset="utf-8">
<title>Glenmorrow – Original Avocado tub wrap</title>
<link rel="stylesheet" href="https://fonts.googleapis.com/css2?family=Cabin+Condensed:wght@400;500&family=Montserrat:wght@400&family=Sofia+Sans+Condensed:ital,wght@1,500&family=Tinos:wght@700&display=swap">
<style>
  :root {
    --tub-green: #7cbb38;
    --tub-green-light: #8fcb42;
    --tub-green-dark: #649e2c;
    --label-frame: #c6f29a;
    --label-frame-edge: #a9dd7c;
    --label-white: #ffffff;
    --rule-green: #7cc23a;
    --logo-green: #5f9a2e;
    --tagline-red: #b5443a;
    --claims-brown: #7a4a1e;
    --ink: #111111;
    --flavour-band: #b8e68d;
  }
  * { margin: 0; padding: 0; box-sizing: border-box; }
  html, body { width: 1200px; height: 1200px; overflow: hidden; }
  body {
    background: linear-gradient(100deg, var(--tub-green-dark) 0%, var(--tub-green-light) 40%, var(--tub-green) 70%, var(--tub-green-dark) 100%);
    position: relative;
  }
  .label-frame {
    position: absolute;
    left: 250px; top: 170px;
    width: 700px; height: 700px;
    border-radius: 56px;
    background: linear-gradient(135deg, var(--label-frame) 0%, var(--label-frame-edge) 100%);
  }
  .label-card {
    position: absolute;
    left: 70px; top: 70px; right: 70px; bottom: 70px;
    border-radius: 44px;
    background: var(--label-white);
    text-align: center;
    padding-top: 40px;
  }
  .product-name {
    font-family: "Sofia Sans Condensed", sans-serif;
    font-style: italic;
    font-weight: 500;
    font-size: 44px;
    line-height: 1.1;
    color: var(--ink);
    text-transform: uppercase;
  }
  .rule {
    width: 340px; height: 4px;
    margin: 18px auto;
    border-radius: 2px;
    background: linear-gradient(90deg, transparent, var(--rule-green) 20%, var(--rule-green) 80%, transparent);
  }
  .brand {
    display: flex; align-items: center; justify-content: center; gap: 12px;
    margin-top: 24px;
  }
  .brand-dot { width: 18px; height: 18px; border-radius: 50%; background: var(--logo-green); }
  .brand-name {
    font-family: "Montserrat", sans-serif;
    font-weight: 400;
    font-size: 50px;
    letter-spacing: 1px;
    color: var(--logo-green);
    text-transform: uppercase;
  }
  .tagline {
    font-family: "Cabin Condensed", sans-serif;
    font-weight: 500;
    font-size: 34px;
    color: var(--tagline-red);
    margin-top: 12px;
  }
  .claims {
    font-family: "Cabin Condensed", sans-serif;
    font-size: 38px;
    line-height: 1.3;
    color: var(--claims-brown);
    margin-top: 10px;
  }
  .flavour {
    position: absolute;
    left: 50%; top: 925px;
    transform: translateX(-50%);
    background: var(--flavour-band);
    padding: 6px 16px;
    font-family: "Tinos", serif;
    font-weight: 700;
    font-size: 34px;
    letter-spacing: 1px;
    color: var(--ink);
    white-space: nowrap;
  }
  .volume {
    position: absolute;
    left: 0; right: 0; top: 995px;
    text-align: center;
    font-family: "Tinos", serif;
    font-weight: 700;
    font-size: 32px;
    color: var(--ink);
  }
  .e-mark { font-size: 38px; font-weight: 700; }
</style>
</head>
<body>
  <section class="label-frame">
    <div class="label-card">
      <h1 class="product-name">Coconut and Avocado<br>Ice Cream</h1>
      <div class="rule"></div>
      <div class="brand">
        <span class="brand-name">Glenmorrow</span>
        <span class="brand-dot"></span>
      </div>
      <p class="tagline">Good Days Taste Green</p>
      <div class="rule"></div>
      <p class="claims">•vegan•dairy free•gluten free•<br>• refined sugar free•<br>•frozen desert•</p>
    </div>
  </section>
  <p class="flavour">ORIGINAL AVOCADO</p>
  <p class="volume">500 ml<span class="e-mark">℮</span></p>
</body>
</html>
```